Looking to Redesign Vemblorix.com website

You guys did one of the brochures for vemblorix.com and I would like to see if we can go ahead and get an estimate for a redesigned web site for the company. We currently have a couple of pages on vemblorix.com which are very much a starter type site.

The new design will need to reflect some of the things discussed in the brochure. It will have flash. Needs to be designed for simple hosting using cpanels.

The site needs to have between 12 and 15 pages with flash pages to move through features. Integrated with twitter like it is now, and contact forms delivered from our CRM along with other interactive features such as subscription to newsletter, etc...

I don't have lots of details on how to proceed yet, but here are some competitor sites:

Can we take a look at potential costs involved in the redo of the site as vague as my description above can permit.

Business to Business

Sans Serif

Must have
• Must have professional feel. Similar to brochure. and logo.
• Include our story in the discussion.
• embedded links to our CRM for popup contact forms.
• Logo files and 2 types of brochures uploaded.
• Important to keep color scheme
Nice to have
• Flash and some movement
Should not have
• Not sure yet

```html
<!DOCTYPE html>
<html lang="en">
<head>
<meta charset="utf-8">
<title>Vemblorix Universal Communication</title>
<link href="https://fonts.googleapis.com/css2?family=Russo+One&family=Raleway:wght@400;500;600;700&family=Arimo:wght@400;700&display=swap" rel="stylesheet">
<style>
:root{
  --red:#c4000b;
  --red-dark:#8d0008;
  --ink:#222222;
  --charcoal:#262626;
  --grey-bg:#efefef;
  --text:#3c3c3c;
  --white:#ffffff;
  --muted:#cfcfcf;
}
*{margin:0;padding:0;box-sizing:border-box}
html,body{width:1200px;height:3125px;overflow:hidden;background:var(--white)}
body{position:relative;font-family:"Raleway",sans-serif;color:var(--text)}
.abs{position:absolute}
svg.band{position:absolute;left:0;display:block}

/* header */
.site-header{position:absolute;left:0;top:0;width:1200px;height:146px;background:var(--white)}
.social{display:flex;gap:8px}
.social span{width:28px;height:28px;border-radius:50%;display:block}
.top-social{position:absolute;left:822px;top:21px}
.top-links{position:absolute;left:995px;top:27px;font:700 13px "Arimo",sans-serif;color:var(--white)}
.brand{position:absolute;left:75px;top:62px;display:flex;align-items:center;gap:10px}
.brand .dot{width:34px;height:34px;border-radius:50%;background:var(--red)}
.brand .name{font:700 22px "Raleway",sans-serif;color:var(--ink)}
.main-nav a{position:absolute;top:111px;font:700 13px "Arimo",sans-serif;color:var(--ink);text-decoration:none;letter-spacing:.5px}
.main-nav a.active{left:333px;top:104px;width:82px;height:33px;border-radius:17px;background:var(--red);color:var(--white);text-align:center;line-height:33px}

/* hero */
.hero{position:absolute;left:0;top:146px;width:1200px;height:580px;overflow:hidden}
.hero-photo{position:absolute;inset:0;background:radial-gradient(circle at 62% 35%,#9a9a9a 0%,#5c5c5c 35%,#2f2f2f 75%,#1d1d1d 100%)}
.hero h1{position:absolute;left:75px;top:134px;font:400 31px/44px "Russo One",sans-serif;font-style:italic;color:var(--white);letter-spacing:1px;text-transform:uppercase}
.hero p{position:absolute;left:75px;top:226px;width:430px;font:400 27px/32px "Arimo",sans-serif;color:var(--white)}
.dots{position:absolute;left:74px;top:350px;display:flex;gap:9px}
.dots i{width:12px;height:12px;border-radius:50%;background:var(--white)}
.dots i:first-child{background:var(--red)}

/* shared */
.section-title{position:absolute;display:flex;align-items:center;gap:10px;font:400 27px "Russo One",sans-serif;font-style:italic;color:var(--red);text-transform:uppercase}
.section-title .mark{width:60px;height:32px;border-radius:16px;background:#bdbdbd}
.btn{position:absolute;height:38px;border-radius:19px;font:600 13px/38px "Raleway",sans-serif;color:var(--white);text-align:center;letter-spacing:.5px;text-transform:uppercase}
.btn-dark{background:linear-gradient(#3a3a3a,#151515)}
.btn-red{background:linear-gradient(#d5000d,#a00008)}
.photo-ring{position:absolute;border-radius:50%;border:10px solid var(--red);box-shadow:6px 10px 0 #3b3b3b}

/* about */
.about-text{position:absolute;left:75px;top:823px;width:1055px;font:400 14px/25px "Raleway",sans-serif;color:var(--text)}

/* advantages */
.advantages-bg{top:985px}
.adv-sub{position:absolute;left:433px;top:1133px;font:500 17px "Raleway",sans-serif;color:var(--ink)}
.adv-item{position:absolute;display:flex;gap:16px;width:330px}
.adv-item .ico{flex:none;width:68px;height:68px;border-radius:50%;border:2px solid #333;background:var(--white);display:flex;align-items:center;justify-content:center}
.adv-item h3{font:700 16px "Arimo",sans-serif;color:var(--red);margin:4px 0 6px}
.adv-item p{font:700 14px/23px "Arimo",sans-serif;color:#333}

/* why */
.why-title{color:var(--white)}
.why-text{position:absolute;left:75px;top:1688px;width:700px;font:500 14px/25.5px "Raleway",sans-serif;color:#e4e4e4}

/* features */
.features-sub{position:absolute;left:0;width:1200px;top:2071px;text-align:center;font:500 17px "Raleway",sans-serif;color:var(--ink)}
.feature{position:absolute;width:330px;text-align:center}
.feature .ico{width:94px;height:94px;border-radius:50%;background:radial-gradient(circle at 40% 35%,#e3000e,#b20008);margin:0 auto 26px;display:flex;align-items:center;justify-content:center;box-shadow:0 3px 6px rgba(0,0,0,.25)}
.feature h3{font:400 18px "Arimo",sans-serif;color:var(--red);margin-bottom:8px}
.feature p{font:400 14.5px/23px "Arimo",sans-serif;color:#222;width:290px;margin:0 auto}

/* footer */
.site-footer{position:absolute;left:0;top:2780px;width:1200px;height:272px;background:linear-gradient(#3a3a3a,#2c2c2c)}
.foot-brand{position:absolute;left:75px;top:62px;display:flex;align-items:center;gap:10px}
.foot-brand .dot{width:34px;height:34px;border-radius:50%;background:var(--white)}
.foot-brand .name{font:700 22px "Raleway",sans-serif;color:var(--white)}
.foot-about{position:absolute;left:75px;top:158px;width:340px;font:500 13.5px/25px "Raleway",sans-serif;color:#e0e0e0}
.foot-more{position:absolute;left:75px;top:212px;font:700 13.5px "Raleway",sans-serif;color:var(--white)}
.foot-div{position:absolute;top:50px;width:1px;height:190px;background:#555}
.foot-h{position:absolute;top:62px;font:700 13px "Arimo",sans-serif;color:var(--white);letter-spacing:1px}
.quick-links a{position:absolute;font:500 13px "Raleway",sans-serif;color:#e0e0e0;text-decoration:none}
.field{position:absolute;left:833px;width:292px;height:36px;border-radius:18px;background:var(--white);padding-left:24px;font:400 13px/36px "Raleway",sans-serif;color:#666}
.bottom-bar{position:absolute;left:0;top:3052px;width:1200px;height:73px;background:#1e1e1e}
.copyright{position:absolute;left:75px;top:29px;font:400 12.5px "Raleway",sans-serif;color:#9a9a9a}
.bottom-social{position:absolute;left:985px;top:24px}
</style>
</head>
<body>

<header class="site-header">
  <svg class="band" style="top:0" width="1200" height="146" viewBox="0 0 1200 146">
    <path d="M380 0 H1200 V62 C1000 78 760 44 560 18 C480 8 420 4 380 0Z" fill="#222"/>
    <path d="M560 0 H1200 V48 C1010 62 790 30 560 0Z" fill="var(--red)"/>
  </svg>
  <div class="social top-social" aria-label="Social links">
    <span style="background:#3b5998"></span><span style="background:#2aa3e0"></span><span style="background:#0e76a8"></span><span style="background:#f08a1c"></span>
  </div>
  <div class="top-links">Support &nbsp;/&nbsp; Contact</div>
  <div class="brand"><span class="dot"></span><span class="name">Vemblorix</span></div>
  <nav class="main-nav">
    <a class="active">HOME</a>
    <a style="left:437px">ABOUT</a>
    <a style="left:527px">WHY VEMBLORIX</a>
    <a style="left:690px">FEATURES</a>
    <a style="left:804px">ADVANTAGES</a>
    <a style="left:937px">BEST OF CLASS HARDWARE</a>
  </nav>
</header>

<section class="hero">
  <div class="hero-photo" role="img" aria-label="Photo of a hand touching a glowing network of connected people icons"></div>
  <h1>Nunc dignissim lectus<br>vitae eros</h1>
  <p>Vestibulum ante ipsum primis in faucibus orci luctus et ultrices posuere cubilia....</p>
  <div class="dots"><i></i><i></i><i></i><i></i></div>
  <svg class="band" style="top:430px" width="1200" height="150" viewBox="0 0 1200 150">
    <path d="M0 40 C300 80 700 60 1200 40 V150 H0Z" fill="#1b1b1b"/>
    <path d="M0 70 C350 110 750 50 1200 90 V150 H0Z" fill="var(--red)"/>
    <path d="M0 135 C400 60 800 70 1200 140 V150 H0Z" fill="var(--white)"/>
  </svg>
</section>

<section class="about">
  <div class="section-title" style="left:75px;top:765px"><span class="mark"></span>About us</div>
  <p class="about-text">Vemblorix Universal Communication was born out of the desire to offer reliable, affordable phone systems for the small- to medium-sized business. Since 2003, we have offered hosted VOIP PBX and call routing services, but they were bundled with larger IT services. As such, it was only cost-effective for the large corporate client.</p>
  <div class="btn btn-dark" style="left:75px;top:929px;width:152px">Read more</div>
</section>

<section class="advantages">
  <svg class="band advantages-bg" width="1200" height="520" viewBox="0 0 1200 520">
    <path d="M0 70 C300 10 700 0 1200 30 V520 H0Z" fill="var(--grey-bg)"/>
    <path d="M350 20 C700 -5 950 10 1200 40 V65 C950 40 700 25 350 20Z" fill="var(--red)"/>
    <path d="M0 440 C300 520 800 380 1200 470 V520 H0Z" fill="#1f1f1f"/>
    <path d="M0 430 C300 500 800 365 1200 455 V475 C800 385 300 515 0 450Z" fill="var(--red)"/>
  </svg>
  <div class="photo-ring" role="img" aria-label="Photo of a businessman drawing a cloud and devices diagram" style="left:73px;top:1058px;width:300px;height:300px;background:radial-gradient(circle,#a9aebb,#3a4358)"></div>
  <div class="section-title" style="left:433px;top:1089px"><span class="mark"></span>Advantages</div>
  <div class="adv-sub">Discovering your needs, creating solutions that truly work</div>
  <div class="adv-item" style="left:433px;top:1180px">
    <div class="ico"><svg width="26" height="30" viewBox="0 0 26 30"><path d="M2 1h15l7 7v21H2z" fill="var(--red)"/><path d="M7 14h12M7 19h12M7 24h8" stroke="#fff" stroke-width="2"/></svg></div>
    <div><h3>Quick ROI</h3><p>Equipment is included in the service..</p></div>
  </div>
  <div class="adv-item" style="left:795px;top:1180px">
    <div class="ico"><svg width="26" height="30" viewBox="0 0 26 30"><path d="M13 1 L24 5 V14 C24 22 18 27 13 29 C8 27 2 22 2 14 V5Z" fill="var(--red)"/><path d="M13 4 V26 C9 24 5 20 5 14 V7Z" fill="#fff"/></svg></div>
    <div><h3>Secure</h3><p>Encrypted lines</p></div>
  </div>
  <div class="adv-item" style="left:433px;top:1278px">
    <div class="ico"><svg width="30" height="30" viewBox="0 0 30 30"><circle cx="11" cy="18" r="8" fill="none" stroke="var(--red)" stroke-width="5" stroke-dasharray="4 2.3"/><circle cx="23" cy="8" r="5" fill="none" stroke="var(--red)" stroke-width="4" stroke-dasharray="3 1.8"/></svg></div>
    <div><h3>Easy installation</h3><p>Very little business interruption</p></div>
  </div>
  <div class="adv-item" style="left:795px;top:1278px">
    <div class="ico"><svg width="28" height="28" viewBox="0 0 28 28"><circle cx="14" cy="14" r="12" fill="var(--red)"/><circle cx="14" cy="14" r="8" fill="#fff"/><path d="M14 8v6h-4" stroke="var(--red)" stroke-width="2.5" fill="none"/></svg></div>
    <div><h3>Expandable</h3><p>One unit at a time</p></div>
  </div>
  <div class="btn btn-dark" style="left:433px;top:1384px;width:152px">Read more</div>
</section>

<section class="why">
  <svg class="band" style="top:1505px" width="1200" height="480" viewBox="0 0 1200 480">
    <path d="M0 0 C300 60 800 -60 1200 30 V400 C800 360 400 470 0 430Z" fill="var(--charcoal)"/>
  </svg>
  <div class="photo-ring" role="img" aria-label="Photo of smiling business team around a laptop" style="left:800px;top:1515px;width:325px;height:285px;background:radial-gradient(circle,#d9dce2,#7a8190)"></div>
  <div class="section-title why-title" style="left:75px;top:1630px"><span class="mark"></span>Why Vemblorix</div>
  <p class="why-text">Honestly, your office phone system is probably the least sexy thing in your company – the minute the system is down, you're out of business – so you need a phone system that you can count on every minute of every day. But your phone system doesn't have to be boring, it can look great, too! With a sleek design and customized logos, these phones add a distinctive look sitting on the desk. What is even better, is how good this system makes you look to your customers. Whatever image you want to portray.</p>
  <div class="btn btn-red" style="left:75px;top:1864px;width:152px">Read more</div>
</section>

<section class="features">
  <div class="section-title" style="left:480px;top:2004px"><span class="mark"></span>Features</div>
  <div class="features-sub">Unified Communications Sample of Powerful Feature Sets</div>

  <div class="feature" style="left:75px;top:2134px">
    <div class="ico"><svg width="34" height="30" viewBox="0 0 34 30"><path d="M14 3H3v24h11" stroke="#fff" stroke-width="4" fill="none"/><path d="M12 15h13M20 8l8 7-8 7" stroke="#fff" stroke-width="4" fill="none"/></svg></div>
    <h3>Outgoing Call Redundancies</h3><p>Multiple Telecommunications Providers create excellent service redundancies for outgoing calls.</p>
  </div>
  <div class="feature" style="left:437px;top:2134px">
    <div class="ico"><svg width="34" height="30" viewBox="0 0 34 30"><path d="M20 3h11v24H20" stroke="#fff" stroke-width="4" fill="none"/><path d="M3 15h17M13 8l8 7-8 7" stroke="#fff" stroke-width="4" fill="none"/></svg></div>
    <h3>Incoming Call Redundancies</h3><p>Multiple Telecommunications Providers create excellent service redundancies for outgoing calls.</p>
  </div>
  <div class="feature" style="left:798px;top:2134px">
    <div class="ico"><svg width="32" height="32" viewBox="0 0 32 32"><path d="M26 12A11 11 0 0 0 6 11M6 20a11 11 0 0 0 20 1" stroke="#fff" stroke-width="4" fill="none"/><path d="M27 3v10h-10zM5 29V19h10z" fill="#fff"/></svg></div>
    <h3>Implementation Ease</h3><p>Multiple Telecommunications Providers create excellent service redundancies for outgoing calls.</p>
  </div>

  <div class="feature" style="left:75px;top:2397px">
    <div class="ico"><svg width="30" height="32" viewBox="0 0 30 32"><path d="M15 3c-6 0-9 4-9 10v7l-3 4h24l-3-4v-7c0-6-3-10-9-10z" fill="#fff"/><circle cx="15" cy="27" r="3" fill="#fff"/></svg></div>
    <h3>911 Notification</h3><p>Multiple Telecommunications Providers create excellent service redundancies for outgoing calls.</p>
  </div>
  <div class="feature" style="left:437px;top:2397px">
    <div class="ico"><svg width="30" height="30" viewBox="0 0 30 30"><path d="M6 2l6 6-3 4c2 4 5 7 9 9l4-3 6 6-4 4C12 28 2 18 2 6z" fill="#fff"/></svg></div>
    <h3>Advanced Call Management</h3><p>Multiple Telecommunications Providers create excellent service redundancies for outgoing calls.</p>
  </div>
  <div class="feature" style="left:798px;top:2397px">
    <div class="ico"><svg width="26" height="34" viewBox="0 0 26 34"><rect x="8" y="2" width="10" height="18" rx="5" fill="#fff"/><path d="M3 15a10 10 0 0 0 20 0M13 25v6M7 32h12" stroke="#fff" stroke-width="3" fill="none"/></svg></div>
    <h3>Advanced Voicemail</h3><p>Multiple Telecommunications Providers create excellent service redundancies for outgoing calls.</p>
  </div>
</section>

<svg class="band" style="top:2620px" width="1200" height="165" viewBox="0 0 1200 165">
  <path d="M0 15 C300 70 700 110 1200 120 V165 H0Z" fill="#2f2f2f"/>
  <path d="M0 10 C350 60 750 100 1200 95 V130 C750 130 350 100 0 60Z" fill="var(--red)"/>
  <path d="M0 0 C300 40 800 85 1200 75 V0Z" fill="var(--white)"/>
</svg>

<footer class="site-footer">
  <div class="foot-brand"><span class="dot"></span><span class="name">Vemblorix</span></div>
  <p class="foot-about">Vemblorix has been in the business of providing Hosted based PBX services since early 2003.</p>
  <div class="foot-more">Read More</div>
  <div class="foot-div" style="left:433px"></div>
  <div class="foot-div" style="left:808px"></div>
  <div class="foot-h" style="left:465px">QUICK LINKS</div>
  <nav class="quick-links">
    <a style="left:465px;top:90px">Home</a>
    <a style="left:465px;top:121px">About</a>
    <a style="left:465px;top:152px">Why Vemblorix</a>
    <a style="left:465px;top:183px">Features</a>
    <a style="left:465px;top:214px">Advantages</a>
    <a style="left:610px;top:90px">Best Of Class Hardware</a>
    <a style="left:610px;top:121px">Support</a>
    <a style="left:577px;top:152px">Contact Us</a>
  </nav>
  <div class="foot-h" style="left:840px">NEWSLETTER SIGN UP</div>
  <div class="field" style="top:95px">Enter Name</div>
  <div class="field" style="top:138px">Enter Email Address</div>
  <div class="btn btn-red" style="left:1010px;top:193px;width:115px;height:36px;line-height:36px">Sign up</div>
</footer>

<div class="bottom-bar">
  <div class="copyright">© 2015-2016 vemblorix. All Rights Reserved</div>
  <div class="social bottom-social">
    <span style="background:#3b5998"></span><span style="background:#2aa3e0"></span><span style="background:#0e76a8"></span><span style="background:#f08a1c"></span>
  </div>
</div>

</body>
</html>
```